Business Card Design Project

Doctor, Pain Management. Need a new business card design with appointment info on the back. New address is 18 Birchwood Court, Suite 304, Holloway, NJ 07519. Right now I believe the rest of the information is staying the same.

```html
<!DOCTYPE html>
<html lang="en">
<head>
<meta charset="utf-8">
<title>Steadfast Pain Care – Business Card</title>
<link href="https://fonts.googleapis.com/css2?family=Open+Sans:wght@400;600;700&family=Arimo:wght@400&display=swap" rel="stylesheet">
<style>
  :root{
    --backdrop:#676767;
    --card:#ffffff;
    --orange:#e95a0c;
    --ink:#222222;
    --muted:#555555;
    --box:#888888;
  }
  *{box-sizing:border-box;margin:0;padding:0}
  html,body{width:1200px;height:802px;overflow:hidden}
  body{background:var(--backdrop);position:relative;font-family:"Open Sans",sans-serif;color:var(--ink)}
  .card{position:absolute;top:274px;width:443px;height:265px;background:var(--card);overflow:hidden}
  .card--front{left:136px}
  .card--back{left:624px}
  .band{position:absolute;left:0;right:0;bottom:0;height:37px;background:var(--orange);color:#fff;
        display:flex;align-items:center;justify-content:center;font-size:12px;white-space:nowrap}

  /* front */
  .brand{position:absolute;left:22px;top:114px;display:flex;align-items:center;gap:7px;
         font-weight:700;font-size:25px;line-height:1;color:var(--ink);white-space:nowrap}
  .brand-dot{width:12px;height:12px;border-radius:50%;background:var(--orange);flex:none}
  .divider{position:absolute;left:188px;top:84px;width:1px;height:97px;background:var(--muted)}
  .details{position:absolute;left:202px;top:79px;white-space:nowrap}
  .doctor-name{color:var(--orange);font-weight:700;font-size:14.5px;line-height:20px}
  .doctor-title{font-size:12.2px;line-height:17px;margin-bottom:6px}
  .contact{list-style:none;font-size:11.6px;line-height:15.8px}
  .contact li{display:flex;align-items:center;gap:3px}
  .contact svg{width:10px;height:10px;fill:var(--orange);flex:none}

  /* back */
  .back-brand{position:absolute;left:0;right:0;top:35px;display:flex;justify-content:center;align-items:center;gap:7px;
              font-weight:700;font-size:28px;line-height:1;color:var(--ink)}
  .practice-name{position:absolute;left:0;right:0;top:90px;text-align:center;font-family:"Arimo",sans-serif;
                 font-weight:400;font-size:18px;line-height:22px;color:var(--ink)}
  .practice-name .accent{color:var(--orange)}
  .appointment{font-family:"Arimo",sans-serif;font-size:14px;color:var(--muted);white-space:nowrap}
  .field-row{position:absolute;left:38px;display:flex;align-items:baseline;gap:4px;line-height:18px}
  .field-row--for{top:133px;right:55px}
  .field-row--date{top:159px;right:38px}
  .fill{border-bottom:1.5px dotted #777;height:12px;flex:none}
  .fill--wide{flex:1}
  .fill--date{width:108px;margin-right:10px}
  .fill--time{width:98px}
  .days{position:absolute;left:38px;width:373px;top:197px;display:flex;justify-content:space-between;font-size:13.5px;line-height:16px}
  .day{display:flex;align-items:center;gap:4px}
  .box{width:16px;height:16px;border:1.5px solid var(--box);flex:none}
  .card--back .band{height:39px;font-size:11.6px;border-top:2px solid #e3e3e3}
</style>
</head>
<body>
  <section class="card card--front">
    <div class="brand"><span class="brand-dot"></span>Steadfast</div>
    <div class="divider"></div>
    <div class="details">
      <h1 class="doctor-name">DR. LIAN MORROW, M.D., PH.D.</h1>
      <p class="doctor-title">Board Certified Anesthiologist</p>
      <ul class="contact">
        <li><svg viewBox="0 0 10 10"><path d="M1 3.5C1 2 3 1 5 1s4 1 4 2.5L7.5 4.3 7 3H3L2.5 4.3zM2.5 5h5l.8 4H1.7z"/></svg>973.555.0142</li>
        <li><svg viewBox="0 0 10 10"><path d="M3 1h4v2H3zM1 3.5h8v4H7.5V6h-5v1.5H1zM3 6.8h4V9H3z"/></svg>973.555.0187</li>
        <li><svg viewBox="0 0 10 10"><circle cx="5" cy="5" r="4.5"/></svg>www.steadfastpc.com</li>
        <li><svg viewBox="0 0 10 10"><path d="M1 2h8v6H1zM1.8 2.6 5 5.3l3.2-2.7" stroke="#fff" stroke-width=".8"/></svg>steadfast.frontdesk@mailbox.com</li>
      </ul>
    </div>
    <footer class="band">18 Birchwood Court, Suite 304, Holloway, NJ 07519</footer>
  </section>

  <section class="card card--back">
    <div class="back-brand"><span class="brand-dot"></span>Steadfast</div>
    <h2 class="practice-name">Steadfast <span class="accent">Pain</span> Care</h2>
    <div class="appointment">
      <div class="field-row field-row--for"><span>For :</span><span class="fill fill--wide"></span></div>
      <div class="field-row field-row--date"><span>Date :</span><span class="fill fill--date"></span><span>Time :</span><span class="fill fill--time"></span><span>AM / PM</span></div>
      <div class="days">
        <span class="day"><span class="box"></span>MON</span>
        <span class="day"><span class="box"></span>TUE</span>
        <span class="day"><span class="box"></span>WED</span>
        <span class="day"><span class="box"></span>THU</span>
        <span class="day"><span class="box"></span>FRI</span>
        <span class="day"><span class="box"></span>SAT</span>
      </div>
    </div>
    <footer class="band">If unable to keep your appointment, please contact us as soon as possible</footer>
  </section>
</body>
</html>
```